Im starting by seying that i dont speak or write Inglés, i dont speak spanish since i am from Paraguay, im very sorry for That, try my best to get Understood. I am startin a company of e liquids, (electronic cigarrettes). the liquid production is ok but the label is not. i try to do my label here with a graphic designer (friend of mine) but is is very busy esta days and I HAD no time for esta. but have made me one label, that i will atach here, That is nice, but is not that i want, because i tell him the name will be "orvanis" (the first alchemist in the world) i tell him that i wanted to explore themes like magic, vapors, etc. mistery but looking now is kind of boring. I really like something more hip and modern with a design work, What i do know is that i want to put a red wax seal on the top center of the glass bottle (will attach pics) i really really like the tidewell artwork, simple, hip, modern, fix in your mind. will attach pics for Those Who dont know the brand, also like the i want to design for 30 ml bottles made of clear glass with dropper (childproof) approx 40 x 90 milimeters in size. i am starting with 8 flavors, so, the design has to be adaptable for each flavor. It has to say somewere the strength level of nicotine 0 -3-6 - 9 to 12 mg in a creative way, maybe some stairs With the levels and the level it has to say Highlighted somewere USA made with ingredients, with some flag or something in the small font section will be warnings, ingredients and other stuff that i will update tomorrow.

Target Market(s)

quitting smokers, vapers

Requirements
Must have
• network (or maybe other color) wax seal as described in the description i wiil update in soon esta sección
Nice to have

```html
<!DOCTYPE html>
<html lang="en">
<head>
<meta charset="utf-8">
<title>Orvanis E-Liquid Labels</title>
<link href="https://fonts.googleapis.com/css2?family=Roboto+Condensed:wght@400;700&display=swap" rel="stylesheet">
<style>
  :root {
    --backdrop: #a7a7a7;
    --label-white: #ffffff;
    --ink: #1d1d1b;
    --band-strawberry: #e8978e;
    --band-mint: #80c8c3;
    --level-0: #d4d4d4;
    --level-3: #9bc46a;
    --level-6: #1f8a43;
    --level-9: #ec7f23;
    --level-12: #e0261f;
    --emblem-tone: #cfcfcf;
    --flag-tone: #b8434b;
  }
  * { box-sizing: border-box; margin: 0; padding: 0; }
  html, body { width: 1105px; height: 1200px; overflow: hidden; }
  body {
    background: var(--backdrop);
    font-family: "Roboto Condensed", "Arial Narrow", sans-serif;
    color: var(--ink);
    position: relative;
  }
  .label {
    position: absolute;
    left: 101px;
    width: 899px;
    height: 449px;
    background: var(--label-white);
    border-radius: 30px;
    overflow: hidden;
    box-shadow: 6px 8px 14px rgba(0,0,0,0.45);
  }
  .label--strawberry { top: 117px; --band: var(--band-strawberry); }
  .label--mint { top: 634px; --band: var(--band-mint); }
  .label__band { position: absolute; inset: 0; width: 100%; height: 100%; }
  .label__band polygon { fill: var(--band); }

  .warning {
    position: absolute;
    left: 17px; top: 24px;
    width: 238px;
    font-size: 12.6px;
    line-height: 13.6px;
  }
  .warning b { font-weight: 700; }
  .volume {
    position: absolute;
    left: 93px; top: 394px;
    font-size: 27px;
    font-weight: 400;
  }

  .brand {
    position: absolute;
    left: 300px; top: 18px;
    width: 300px;
    text-align: center;
  }
  .brand__name {
    font-size: 66px;
    line-height: 70px;
    font-weight: 400;
    letter-spacing: 1px;
  }
  .brand__type {
    font-size: 21px;
    font-weight: 700;
    line-height: 22px;
    margin-top: 2px;
  }
  .emblem {
    position: absolute;
    left: 315px; top: 128px;
    width: 216px; height: 216px;
    border-radius: 50%;
    background: var(--emblem-tone);
  }

  .strength {
    position: absolute;
    left: 326px; top: 366px;
    width: 250px;
  }
  .strength__values {
    display: flex;
    font-size: 16.5px;
    line-height: 18px;
  }
  .strength__values span { width: 50px; text-align: center; }
  .strength__bar {
    display: flex;
    height: 20px;
    margin-top: 3px;
    border-radius: 10px;
    overflow: hidden;
  }
  .strength__bar span { width: 50px; display: flex; align-items: center; justify-content: center; }
  .strength__bar .l0 { background: var(--level-0); }
  .strength__bar .l3 { background: var(--level-3); }
  .strength__bar .l6 { background: var(--level-6); }
  .strength__bar .l9 { background: var(--level-9); }
  .strength__bar .l12 { background: var(--level-12); }
  .flavor {
    text-align: center;
    font-size: 20px;
    font-weight: 700;
    margin-top: 5px;
  }

  .details {
    position: absolute;
    left: 672px; top: 30px;
    width: 215px;
    font-size: 17.2px;
    line-height: 18.6px;
  }
  .details b { font-weight: 700; }
  .details p + p { margin-top: 19px; }
  .origin {
    position: absolute;
    left: 672px; top: 253px;
    display: flex;
    align-items: center;
    gap: 6px;
  }
  .origin__flag { width: 44px; height: 58px; }
  .origin__text {
    font-size: 17px;
    line-height: 18.5px;
    text-align: center;
    width: 170px;
  }
</style>
</head>
<body>

<section class="label label--strawberry">
  <svg class="label__band" viewBox="0 0 899 449" preserveAspectRatio="none" aria-hidden="true">
    <polygon points="0,427 899,32 899,449 0,449"/>
  </svg>
  <p class="warning"><b>WARNING:</b> Our products may contain nicotine, wich is highly addictive. Not for sale to minors. Product not recommended for pregnant women and people with cardiovascular problems. Lock up an keep out of the reach of children and pets. In case of CONTACT TO SKIN: Wash thoroughly with soap and water. If you feel unwell consult a doctor ASAP, and keep product container or label with you.<br><b>ATENCION:</b> Nuestros productos podrian o no contener nicotina, la cual es altamente adictiva. NO debe venderse a menores. Producto no recomendado para mujeres embarazadas y personas con problemas cardiovasculares. Mantener bajo llave y lejos del alcance de niños y mascotas. En caso de CONTACO CON LA PIEL: lavar con abundante agua y jabon. Si usando este producto se siente mareado y/o con otras molestias, consulte con un Doctor inmediatamente, llevando consigo el envase o la etiqueta de este producto.</p>
  <p class="volume">30ml</p>
  <div class="brand">
    <p class="brand__name">Orvanis</p>
    <p class="brand__type">E-LIQUID</p>
  </div>
  <div class="emblem" role="img" aria-label="Circular alchemical line emblem with nested triangles and radiating rays"></div>
  <div class="strength">
    <div class="strength__values"><span>0mg</span><span>3mg</span><span>6mg</span><span>9mg</span><span>12mg</span></div>
    <div class="strength__bar">
      <span class="l0"></span><span class="l3"></span><span class="l6"></span><span class="l9"></span>
      <span class="l12"><svg width="22" height="14" viewBox="0 0 22 14" aria-hidden="true"><polyline points="2,7 8,12 20,2" fill="none" stroke="#fff" stroke-width="2.2" stroke-linecap="round" stroke-linejoin="round"/></svg></span>
    </div>
    <p class="flavor">STRAWBERRY</p>
  </div>
  <div class="details">
    <p><b>INGREDIENTS:</b> USP Vegetable Glycerin, USP Propylene Glycol, Natural and Artificial food Flavorings.</p>
    <p><b>Manufactured by:</b> Orvanis Ltd, Corvel Park, Ashby Trade Center USA<br>info@orvanis.com<br>www.orvanis.com</p>
  </div>
  <div class="origin">
    <svg class="origin__flag" viewBox="0 0 44 58" role="img" aria-label="Droplet with USA flag">
      <path d="M22 2 C14 16 3 26 3 38 A19 19 0 0 0 41 38 C41 26 30 16 22 2 Z" fill="var(--flag-tone)"/>
    </svg>
    <p class="origin__text">Made with ingredients from the USA</p>
  </div>
</section>

<section class="label label--mint">
  <svg class="label__band" viewBox="0 0 899 449" preserveAspectRatio="none" aria-hidden="true">
    <polygon points="0,427 899,32 899,449 0,449"/>
  </svg>
  <p class="warning"><b>WARNING:</b> Our products may contain nicotine, wich is highly addictive. Not for sale to minors. Product not recommended for pregnant women and people with cardiovascular problems. Lock up an keep out of the reach of children and pets. In case of CONTACT TO SKIN: Wash thoroughly with soap and water. If you feel unwell consult a doctor ASAP, and keep product container or label with you.<br><b>ATENCION:</b> Nuestros productos podrian o no contener nicotina, la cual es altamente adictiva. NO debe venderse a menores. Producto no recomendado para mujeres embarazadas y personas con problemas cardiovasculares. Mantener bajo llave y lejos del alcance de niños y mascotas. En caso de CONTACO CON LA PIEL: lavar con abundante agua y jabon. Si usando este producto se siente mareado y/o con otras molestias, consulte con un Doctor inmediatamente, llevando consigo el envase o la etiqueta de este producto.</p>
  <p class="volume">30ml</p>
  <div class="brand">
    <p class="brand__name">Orvanis</p>
    <p class="brand__type">E-LIQUID</p>
  </div>
  <div class="emblem" role="img" aria-label="Circular alchemical line emblem with nested triangles and radiating rays"></div>
  <div class="strength">
    <div class="strength__values"><span>0mg</span><span>3mg</span><span>6mg</span><span>9mg</span><span>12mg</span></div>
    <div class="strength__bar">
      <span class="l0"></span><span class="l3"></span><span class="l6"></span><span class="l9"></span>
      <span class="l12"><svg width="22" height="14" viewBox="0 0 22 14" aria-hidden="true"><polyline points="2,7 8,12 20,2" fill="none" stroke="#fff" stroke-width="2.2" stroke-linecap="round" stroke-linejoin="round"/></svg></span>
    </div>
    <p class="flavor">MINT</p>
  </div>
  <div class="details">
    <p><b>INGREDIENTS:</b> USP Vegetable Glycerin, USP Propylene Glycol, Natural and Artificial food Flavorings.</p>
    <p><b>Manufactured by:</b> Orvanis Ltd, Corvel Park, Ashby Trade Center USA<br>info@orvanis.com<br>www.orvanis.com</p>
  </div>
  <div class="origin">
    <svg class="origin__flag" viewBox="0 0 44 58" role="img" aria-label="Droplet with USA flag">
      <path d="M22 2 C14 16 3 26 3 38 A19 19 0 0 0 41 38 C41 26 30 16 22 2 Z" fill="var(--flag-tone)"/>
    </svg>
    <p class="origin__text">Made with ingredients from the USA</p>
  </div>
</section>

</body>
</html>
```